Corinne Dabney Interiors business cards

We need a DOUBLE SIDED business card design that is simple, elegant and modern. We are a rapidly growing Interior Design Firm, and our brand colours are blush pink, navy, and antique gold, so we require some or all of these colours to be used. The final design should portray elegance, simplicity, and have a modern feel. We have upload inspiration photos that have the feel we're looking for.

Industry/Entity Type

Interior Design

Contact Information for Business Card

Contact information and LOGO

Colors
EB3D1F
EC4F4E
F09395
F8D3D4
FCEDEE

Requirements
Must have
• Navy, the right shade of blush pink, and antique gold

```html
<!DOCTYPE html>
<html lang="en">
<head>
<meta charset="utf-8">
<title>Corinne Dabney Interiors – Business Cards</title>
<link rel="stylesheet" href="https://fonts.googleapis.com/css2?family=Jost:wght@300;400&display=swap">
<style>
  :root {
    --bg: #d9d9d9;
    --card: #ffffff;
    --blush: #e8b4b0;
    --navy: #2e3866;
    --gold: #a8802f;
    --mauve: #8a6f86;
  }
  * { margin: 0; padding: 0; box-sizing: border-box; }
  html, body { width: 1200px; height: 800px; overflow: hidden; }
  body {
    background: var(--bg);
    font-family: "Jost", "Helvetica Neue", Arial, sans-serif;
    position: relative;
  }
  .card {
    position: absolute;
    width: 520px;
    height: 300px;
    background: var(--card);
    overflow: hidden;
    box-shadow: 0 6px 18px rgba(0,0,0,0.12);
  }
  .card-front { left: 50px; top: 100px; }
  .card-back { left: 630px; top: 400px; }
  .card-shapes { position: absolute; inset: 0; width: 100%; height: 100%; }

  .brand {
    position: absolute;
    display: flex;
    align-items: center;
    gap: 10px;
    color: var(--gold);
    font-weight: 400;
    text-transform: uppercase;
    white-space: nowrap;
  }
  .brand-mark { background: var(--navy); flex: none; }
  .card-front .brand {
    left: 50%; top: 50%;
    transform: translate(-50%, -50%);
    font-size: 19px;
    letter-spacing: 0.04em;
  }
  .card-front .brand-mark { width: 16px; height: 16px; }

  .logo-tile {
    position: absolute;
    left: 296px; top: 82px;
    width: 170px; height: 128px;
    background: var(--card);
    border: 4px solid var(--navy);
    border-image: linear-gradient(135deg, var(--navy), var(--mauve)) 1;
    transform: rotate(-18deg);
  }
  .logo-tile .brand {
    left: 50%; top: 50%;
    transform: translate(-50%, -50%);
    font-size: 9.5px;
    gap: 6px;
  }
  .logo-tile .brand-mark { width: 8px; height: 8px; }

  .person {
    position: absolute;
    left: 36px; top: 58px;
    color: var(--navy);
  }
  .person-name {
    font-weight: 300;
    font-size: 40px;
    line-height: 0.95;
    text-transform: uppercase;
    letter-spacing: 0.01em;
  }
  .person-title {
    margin-top: 8px;
    font-size: 10px;
    letter-spacing: 0.28em;
    text-transform: uppercase;
  }
  .contact {
    position: absolute;
    left: 36px; top: 190px;
    color: var(--navy);
    font-size: 12px;
    line-height: 1.3;
    list-style: none;
  }
  .contact-social { margin-top: 10px; }
  .contact-social li { display: flex; align-items: center; gap: 7px; }
  .social-dot {
    width: 9px; height: 9px;
    border: 1px solid var(--navy);
    border-radius: 50%;
    flex: none;
  }
</style>
</head>
<body>

  <section class="card card-front" aria-label="Card front">
    <svg class="card-shapes" viewBox="0 0 520 300" aria-hidden="true">
      <polygon points="0,70 0,300 115,300" fill="var(--blush)"/>
      <polygon points="410,0 520,0 520,250" fill="var(--blush)"/>
    </svg>
    <div class="brand"><span class="brand-mark"></span>Corinne Dabney Interiors</div>
  </section>

  <section class="card card-back" aria-label="Card back">
    <svg class="card-shapes" viewBox="0 0 520 300" aria-hidden="true">
      <polygon points="260,0 520,0 520,300 420,300 360,90" fill="var(--blush)"/>
      <polygon points="420,0 520,0 520,250" fill="var(--navy)"/>
    </svg>

    <div class="person">
      <h1 class="person-name">Corinne<br>Dabney</h1>
      <p class="person-title">Principle Designer</p>
    </div>

    <ul class="contact">
      <li>Office: #555-014-2738</li>
      <li>corinne@cdinteriorsinc.com</li>
      <li>www.corinnedabneyinteriors.com</li>
      <li class="contact-social">
        <ul>
          <li><span class="social-dot"></span>corinnedabneyinteriors</li>
          <li><span class="social-dot"></span>corinne.dabney.interiors</li>
        </ul>
      </li>
    </ul>

    <div class="logo-tile">
      <div class="brand"><span class="brand-mark"></span>Corinne Dabney Interiors</div>
    </div>
  </section>

</body>
</html>
```